letterhead, envelope & business card
Letterhead:
Maple Dwelling Depot
3842 Larkspur Lane Bozeman, MT 59718
Phone #: (406) 555-0148
Fax#: (406) 555-0193
Business cards:
Maple Dwelling Depot
Phone #: (406) 555-0148
Fax#: (406) 555-0193
Corinne Baxley
corinne@mapledwellingdepot.example
www.mapledwellingdepot.example
Target Market(s)
Home Interiors client
Industry/Entity Type
Business
Requirements
Must have
- ONLY submit straight front view on white background
- I DO NOT WANT ANY MOCK UPS
Nice to have
- see attached logo use guide
Should not have

```html
<!DOCTYPE html>
<html lang="en">
<head>
<meta charset="utf-8">
<title>Maple Dwelling Depot – Business Card</title>
<link rel="stylesheet" href="https://fonts.googleapis.com/css2?family=Bebas+Neue&family=Lato:wght@400;700&display=swap">
<style>
  :root {
    --page: #ffffff;
    --card-front: #ffffff;
    --card-back: #666666;
    --brand-blue: #1677c2;
    --text-gray: #555555;
    --text-light: #ffffff;
  }
  html, body {
    margin: 0;
    padding: 0;
    width: 1200px;
    height: 1000px;
    overflow: hidden;
    background: var(--page);
    font-family: "Lato", sans-serif;
  }
  .canvas { position: relative; width: 1200px; height: 1000px; }
  .card {
    position: absolute;
    width: 518px;
    height: 305px;
    box-shadow: 0 14px 28px rgba(0,0,0,0.22), 0 4px 10px rgba(0,0,0,0.08);
  }
  .card--front { left: 347px; top: 149px; background: var(--card-front); }
  .card--back { left: 347px; top: 529px; background: var(--card-back); }

  .identity {
    position: absolute;
    right: 274px;
    top: 128px;
    text-align: right;
  }
  .identity__name {
    font-family: "Bebas Neue", sans-serif;
    font-size: 29px;
    line-height: 1;
    color: var(--brand-blue);
    letter-spacing: 0.2px;
  }
  .identity__title {
    font-size: 12px;
    color: var(--text-gray);
    margin-top: 2px;
  }
  .divider {
    position: absolute;
    left: 258px;
    top: 121px;
    width: 1.5px;
    height: 62px;
    background: var(--brand-blue);
  }
  .contacts {
    position: absolute;
    left: 276px;
    top: 117px;
    margin: 0;
    padding: 0;
    list-style: none;
  }
  .contacts__item {
    display: flex;
    align-items: center;
    height: 17.5px;
    font-size: 12px;
    color: var(--text-gray);
  }
  .contacts__icon { width: 10px; height: 10px; margin-right: 7px; flex: none; }
  .address {
    position: absolute;
    left: 0;
    right: 0;
    top: 271px;
    text-align: center;
    font-size: 12px;
    color: var(--text-gray);
  }
  .address__company { color: var(--brand-blue); }

  .wordmark {
    position: absolute;
    left: 0;
    right: 0;
    top: 160px;
    display: flex;
    justify-content: center;
    align-items: center;
    gap: 12px;
  }
  .wordmark__square { width: 16px; height: 16px; background: var(--brand-blue); }
  .wordmark__name {
    font-size: 26px;
    font-weight: 700;
    letter-spacing: 1px;
    color: var(--text-light);
    text-transform: uppercase;
  }
</style>
</head>
<body>
<div class="canvas">
  <section class="card card--front">
    <div class="identity">
      <div class="identity__name">Corinne Baxley</div>
      <div class="identity__title">General Manager</div>
    </div>
    <div class="divider"></div>
    <ul class="contacts">
      <li class="contacts__item">
        <svg class="contacts__icon" viewBox="0 0 10 10"><path d="M2 1 L4 3 L3 4 Q4 6 6 7 L7 6 L9 8 L8 9.5 Q3 9 0.5 2 Z" fill="var(--brand-blue)"/></svg>
        (406) 555-0148
      </li>
      <li class="contacts__item">
        <svg class="contacts__icon" viewBox="0 0 10 10"><rect x="2.5" y="1" width="5" height="3" fill="var(--brand-blue)"/><rect x="0.5" y="4" width="9" height="4" rx="1" fill="var(--brand-blue)"/><rect x="2.5" y="6.5" width="5" height="3" fill="#fff" stroke="var(--brand-blue)"/></svg>
        (406) 555-0193
      </li>
      <li class="contacts__item">
        <svg class="contacts__icon" viewBox="0 0 10 10"><rect x="0.5" y="2" width="9" height="6.5" fill="var(--brand-blue)"/><path d="M0.5 2 L5 6 L9.5 2" fill="none" stroke="#fff" stroke-width="0.9"/></svg>
        corinne@mapledwellingdepot.example
      </li>
      <li class="contacts__item">
        <svg class="contacts__icon" viewBox="0 0 10 10"><g fill="none" stroke="var(--brand-blue)" stroke-width="0.8"><circle cx="5" cy="5" r="4.3"/><ellipse cx="5" cy="5" rx="2" ry="4.3"/><line x1="0.7" y1="5" x2="9.3" y2="5"/></g></svg>
        www.mapledwellingdepot.example
      </li>
    </ul>
    <div class="address"><span class="address__company">Maple Dwelling Depot:</span> 3842 Larkspur Lane Bozeman, MT 59718</div>
  </section>

  <section class="card card--back">
    <div class="wordmark">
      <span class="wordmark__square"></span>
      <span class="wordmark__name">Maple Dwelling Depot</span>
    </div>
  </section>
</div>
</body>
</html>
```